Mara Lindqvist Advisory Business Cards

Hi - using the information and logo provided I require a two sided business card designed with the following information. The business card is a 'mini card' 3.5" x 1.25".

Front of card should be the logo attached but inverted (so the background is the peach colour and the logo white).

Back should have these details. If we can't fit the Instragram and Facebook part can we just put the little logos.

Mara Lindqvist

Art and Design Consultant
Dealer - Curator - Events - Styling - Creative Sourcing

P: 0438 519 207
E: mara@maralindqvistadvisory.com
W: www.maralindqvistadvisory.com
I (instagram image please): maralindqvistadvisory F (Facebook image please): MaraLindqvistAdvisor

Target Market(s)

Galleries, artists, art buyers, interior design clients, event managers, creative types

Industry/Entity Type

Business

```html
<!DOCTYPE html>
<html lang="en">
<head>
<meta charset="utf-8">
<title>Mara Lindqvist Advisory – Mini Business Card</title>
<link rel="stylesheet" href="https://fonts.googleapis.com/css2?family=Cormorant+Garamond:wght@400;500&family=Questrial&display=swap">
<style>
  :root {
    --backdrop: #8c8c8c;
    --peach: #f6bb9b;
    --white: #ffffff;
    --paper: #f4f4f6;
    --ink: #555557;
  }
  * { box-sizing: border-box; margin: 0; padding: 0; }
  html, body {
    width: 1200px;
    height: 1098px;
    overflow: hidden;
    background: var(--backdrop);
  }
  .card {
    position: absolute;
    left: 92px;
    width: 992px;
    height: 354px;
  }
  .card--front {
    top: 149px;
    background: var(--peach);
    display: flex;
    align-items: center;
    justify-content: center;
  }
  .card--back {
    top: 588px;
    background: var(--paper);
    color: var(--ink);
    font-family: "Questrial", sans-serif;
  }
  .brand-name {
    font-family: "Cormorant Garamond", serif;
    font-weight: 500;
    white-space: nowrap;
  }
  .card--front .brand-name {
    color: var(--white);
    font-size: 46px;
    letter-spacing: 1px;
  }
  .card--back .brand-name {
    position: absolute;
    left: 41px;
    top: 62px;
    font-size: 26px;
    color: var(--peach);
  }
  .holder {
    position: absolute;
    left: 41px;
    top: 212px;
  }
  .holder__name {
    font-family: "Cormorant Garamond", serif;
    font-weight: 500;
    font-size: 46px;
    line-height: 1;
    color: var(--peach);
  }
  .holder__role {
    margin-top: 12px;
    font-size: 25px;
    line-height: 1;
  }
  .holder__services {
    margin-top: 10px;
    font-size: 17px;
    line-height: 1;
    letter-spacing: 0.2px;
  }
  .contact {
    position: absolute;
    right: 41px;
    list-style: none;
    text-align: right;
    font-size: 25px;
    line-height: 1;
  }
  .contact--direct { top: 66px; }
  .contact--direct li + li { margin-top: 19px; }
  .contact--social { top: 230px; }
  .contact--social li + li { margin-top: 21px; }
  .contact--social li {
    display: flex;
    align-items: center;
    justify-content: flex-end;
    gap: 12px;
  }
  .social-mark {
    width: 28px;
    height: 28px;
    background: var(--peach);
    flex: none;
  }
</style>
</head>
<body>
  <section class="card card--front" aria-label="Card front">
    <span class="brand-name">Mara Lindqvist Advisory</span>
  </section>

  <section class="card card--back" aria-label="Card back">
    <span class="brand-name">Mara Lindqvist Advisory</span>

    <div class="holder">
      <p class="holder__name">Mara Lindqvist</p>
      <p class="holder__role">Art and Design Consultant</p>
      <p class="holder__services">Dealer - Curator - Events - Styling - Creative Sourcing</p>
    </div>

    <ul class="contact contact--direct">
      <li>0438 519 207</li>
      <li>mara@maralindqvistadvisory.com</li>
      <li>www.maralindqvistadvisory.com</li>
    </ul>

    <ul class="contact contact--social">
      <li>maralindqvistadvisory <span class="social-mark"></span></li>
      <li>MaraLindqvistAdvisor <span class="social-mark"></span></li>
    </ul>
  </section>
</body>
</html>
```